Business card

We are looking for a creative person to deigns our company business card.

Target Market(s)

College age student

Industry/Entity Type

Accommodation

Contact Information for Business Card

We want a fun, clean and sophisticated design. It should look good, but more importantly the information should be legible.

Font styles to use
Serif
Sans Serif
Other font styles liked:
• Open Sans ,

Colors
33a6d7

Requirements
Must have
• Must have a young and memorable message. Be legible.
• Our logo on the back on a solid blue , please find color and logo attached
• LodgeBridgely.net on the back.
Nice to have
• I would like to have couple of different fonts on the LodgeBridgely.net on the back of the cards with a solid blue.

```html
<!DOCTYPE html>
<html lang="en">
<head>
<meta charset="utf-8">
<title>LodgeBridgely Business Card</title>
<link href="https://fonts.googleapis.com/css2?family=Open+Sans:wght@400;600;700;800&display=swap" rel="stylesheet">
<style>
  :root {
    --brand-blue: #33a6d7;
    --deep-blue: #0a6aa6;
    --navy-blue: #0b5a8f;
    --band-blue: #3c9fd0;
    --paper: #ffffff;
    --paper-shade: #eef1f3;
    --stage: #e7e9ec;
    --ink-light: #ffffff;
  }
  html, body {
    margin: 0;
    padding: 0;
    width: 1200px;
    height: 780px;
    overflow: hidden;
    background: var(--stage);
    font-family: "Open Sans", Arial, sans-serif;
  }
  .canvas {
    position: relative;
    width: 1200px;
    height: 780px;
    display: flex;
    align-items: center;
    justify-content: center;
    gap: 90px;
  }
  .card {
    position: relative;
    width: 360px;
    height: 620px;
    border-radius: 24px;
    overflow: hidden;
    box-shadow: 0 10px 30px rgba(0, 0, 0, 0.18);
  }
  /* Front */
  .card-front { background: var(--paper); }
  .front-art {
    position: absolute;
    inset: 0;
  }
  .brand-lockup {
    position: absolute;
    top: 150px;
    left: 0;
    right: 0;
    display: flex;
    align-items: center;
    justify-content: center;
    gap: 10px;
  }
  .brand-square {
    width: 22px;
    height: 22px;
    background: var(--brand-blue);
  }
  .brand-name {
    font-weight: 700;
    font-size: 30px;
    color: var(--brand-blue);
    letter-spacing: -0.5px;
  }
  .contact {
    position: absolute;
    top: 318px;
    left: 0;
    right: 0;
    text-align: center;
    color: var(--ink-light);
  }
  .contact p { margin: 0; }
  .person-name {
    font-weight: 800;
    font-size: 22px;
    letter-spacing: 1px;
    line-height: 1.1;
  }
  .contact .person-role {
    font-size: 15px;
    margin-bottom: 14px;
    line-height: 1.1;
  }
  .contact-label {
    font-weight: 700;
    font-size: 13px;
    line-height: 1.2;
  }
  .contact .contact-value {
    font-size: 16px;
    margin-bottom: 10px;
    line-height: 1.25;
  }
  .divider {
    width: 230px;
    height: 1px;
    background: rgba(255, 255, 255, 0.55);
    margin: 0 auto 10px;
  }
  .address { font-size: 16px; line-height: 1.3; }
  .website {
    position: absolute;
    top: 565px;
    left: 0;
    right: 0;
    height: 55px;
    margin: 0;
    display: flex;
    align-items: center;
    justify-content: center;
    font-size: 17px;
    color: var(--ink-light);
    letter-spacing: 0.3px;
  }
  /* Back */
  .card-back {
    background: radial-gradient(ellipse at 55% 45%, #0e7bbd 0%, var(--deep-blue) 50%, var(--navy-blue) 100%);
  }
  .back-lockup {
    position: absolute;
    top: 50%;
    left: 50%;
    transform: translate(-50%, -50%) rotate(90deg);
    display: flex;
    align-items: center;
    gap: 14px;
    white-space: nowrap;
  }
  .back-square {
    width: 26px;
    height: 26px;
    background: var(--ink-light);
  }
  .back-name {
    font-weight: 700;
    font-size: 34px;
    color: var(--ink-light);
    letter-spacing: -0.5px;
  }
</style>
</head>
<body>
<main class="canvas">
  <section class="card card-front" aria-label="Card front">
    <svg class="front-art" width="360" height="620" viewBox="0 0 360 620" aria-hidden="true">
      <defs>
        <linearGradient id="bodyBlue" x1="0" y1="0" x2="0" y2="1">
          <stop offset="0" stop-color="#1486c4"/>
          <stop offset="1" stop-color="#0a6aa6"/>
        </linearGradient>
        <linearGradient id="topPaper" x1="0" y1="0" x2="0" y2="1">
          <stop offset="0" stop-color="#ffffff"/>
          <stop offset="1" stop-color="#eef1f3"/>
        </linearGradient>
      </defs>
      <rect width="360" height="620" fill="url(#topPaper)"/>
      <path d="M0 255 C 120 235, 260 250, 360 330 L 360 620 L 0 620 Z" fill="#33a6d7"/>
      <path d="M0 265 C 120 248, 260 262, 360 345 L 360 620 L 0 620 Z" fill="url(#bodyBlue)"/>
      <path d="M40 282 C 150 270, 270 290, 350 352" fill="none" stroke="#ffffff" stroke-width="3" opacity="0.9"/>
      <rect x="0" y="565" width="360" height="55" fill="#3c9fd0"/>
      <rect x="0" y="561" width="360" height="4" fill="#ffffff" opacity="0.85"/>
    </svg>

    <div class="brand-lockup">
      <span class="brand-square"></span>
      <span class="brand-name">LodgeBridgely</span>
    </div>

    <div class="contact">
      <p class="person-name">MARA QUINLAN</p>
      <p class="person-role">CEO</p>
      <p class="contact-label">Phone:</p>
      <p class="contact-value">555 014 2368</p>
      <div class="divider"></div>
      <p class="contact-label">Email:</p>
      <p class="contact-value">hello@lodgebridgely.net</p>
      <div class="divider"></div>
      <p class="address">PO BOX 482 Harlow Lane<br>4th street Fernvale</p>
    </div>

    <p class="website">www.lodgebridgely.net</p>
  </section>

  <section class="card card-back" aria-label="Card back">
    <div class="back-lockup">
      <span class="back-name">LodgeBridgely</span>
      <span class="back-square"></span>
    </div>
  </section>
</main>
</body>
</html>
```